Vela Craft 3D - Stationary Design
3D Printing and Design Company
Project: Vela Craft 3D - Stationary Design
Vela Craft 3D - Stationary Design - Engineering
Creative Brief
Bright & Fun-filled
Marcus Pellington
Lead Designer
PO Box 862 Harwell, MA 01748
Marcus@VelaCraft3D.com
VelaCraft3D.com
mp71rqz mp71rqz
I forgot to mention that I would like the back to have a design to it but I want it to be generic text to be added later. A Paragraph or so. Thank you!

```html
<!DOCTYPE html>
<html lang="en">
<head>
<meta charset="utf-8">
<title>Vela Craft 3D — Business Card</title>
<link href="https://fonts.googleapis.com/css2?family=PT+Sans:wght@400;700&display=swap" rel="stylesheet">
<style>
  :root {
    --backdrop: #d9d9d9;
    --card: #0b0b0b;
    --card-edge: #1c1c1c;
    --gold: #f0a81c;
    --gold-line: #c98a12;
    --text-light: #e6e6e6;
    --text-muted: #9a9a9a;
    --ghost: #1a1a1a;
  }
  * { box-sizing: border-box; margin: 0; padding: 0; }
  html, body { width: 1200px; height: 799px; overflow: hidden; }
  body {
    background: var(--backdrop);
    font-family: "PT Sans", sans-serif;
    position: relative;
  }
  .card {
    position: absolute;
    top: 251px;
    width: 520px;
    height: 297px;
    border-radius: 24px;
    background: var(--card);
    border: 1px solid var(--card-edge);
    overflow: hidden;
  }
  .card--back { left: 50px; }
  .card--front { left: 630px; }

  /* back */
  .back__mark {
    position: absolute;
    left: 170px; top: 70px;
    width: 180px; height: 180px;
    border-radius: 50%;
    background: var(--ghost);
  }
  .back__copy {
    position: absolute;
    left: 60px; right: 50px; top: 72px;
    color: var(--text-light);
    font-size: 14px;
    line-height: 1.5;
  }
  .back__copy p + p { margin-top: 16px; }

  /* front */
  .front__brand {
    position: absolute;
    right: 34px; top: 40px;
    display: flex; align-items: center; gap: 10px;
    color: var(--gold);
    font-weight: 700;
    font-size: 34px;
    letter-spacing: -0.5px;
  }
  .front__brand-dot {
    width: 26px; height: 26px; border-radius: 50%;
    background: var(--gold);
  }
  .front__person {
    position: absolute;
    left: 30px; top: 148px;
    width: 226px;
    text-align: right;
  }
  .front__name {
    color: var(--gold);
    font-size: 23px;
    font-weight: 700;
    line-height: 1.1;
  }
  .front__role {
    color: var(--text-muted);
    font-size: 19px;
    margin-top: 2px;
  }
  .front__divider {
    position: absolute;
    left: 272px; top: 138px;
    width: 2px; height: 112px;
    background: var(--gold-line);
  }
  .front__contact {
    position: absolute;
    left: 292px; top: 140px;
    list-style: none;
    color: var(--text-light);
    font-size: 11.5px;
    line-height: 1.45;
  }
  .front__contact li { display: flex; align-items: center; gap: 6px; }
  .front__contact .address { display: block; margin-bottom: 6px; }
  .front__contact svg { flex: none; }
</style>
</head>
<body>

<section class="card card--back" aria-label="Card back">
  <div class="back__mark" aria-hidden="true"></div>
  <div class="back__copy">
    <p>Lorem ipsum dolor sit amet, consectetur adipiscing elit. Duis augue odio, accumsan sit amet bibendum non, mollis eget nulla. Maecenas eget justo quam.</p>
    <p>Lorem ipsum dolor sit amet, consectetur adipiscing elit. Duis augue odio, accumsan sit amet bibendum non, mollis eget nulla. Maecenas eget justo quam.</p>
  </div>
</section>

<section class="card card--front" aria-label="Card front">
  <div class="front__brand">
    <span>Vela Craft 3D</span>
    <span class="front__brand-dot" aria-hidden="true"></span>
  </div>

  <div class="front__person">
    <div class="front__name">Marcus Pellington</div>
    <div class="front__role">Lead Designer</div>
  </div>

  <div class="front__divider" aria-hidden="true"></div>

  <ul class="front__contact">
    <li class="address">PO Box 862<br>Harwell, MA 01748</li>
    <li>
      <svg width="9" height="9" viewBox="0 0 9 9" aria-hidden="true"><circle cx="4.5" cy="4.5" r="4" fill="var(--gold)"/></svg>
      508-555-0142
    </li>
    <li>
      <svg width="9" height="9" viewBox="0 0 9 9" aria-hidden="true"><circle cx="4.5" cy="4.5" r="4" fill="var(--gold)"/></svg>
      Marcus@VelaCraft3D.com
    </li>
    <li>
      <svg width="9" height="9" viewBox="0 0 9 9" aria-hidden="true"><circle cx="4.5" cy="4.5" r="4" fill="var(--gold)"/></svg>
      VelaCraft3D.com
    </li>
  </ul>
</section>

</body>
</html>
```